Harrow Peak Lending Business Cards

please see business card design and compass logo design. please make the blue a bit lighter

Contact Information for Business Card

Dana Whitfield
Proprietor
Dip Finance & Mortgage Broking Management (this can be shortened)
LBQC
ACR *****
ABN ****
Mobile
Email

Logo Text

home, business, asset finance

Colors
ffcf3e
ffc214
33a6d7
85acd3
3277b5
ffffff

Requirements
Should not have
• pictures of oceans or cities. I am not trying to replicate a fishing company

```html
<!DOCTYPE html>
<html lang="en">
<head>
<meta charset="utf-8">
<title>Harrow Peak Lending — Business Cards</title>
<link rel="stylesheet" href="https://fonts.googleapis.com/css2?family=Tenor+Sans&family=Fira+Sans:wght@400;500&family=Montserrat:wght@400&display=swap">
<style>
  :root {
    --backdrop: #021f33;
    --card-front: #ffffff;
    --card-back: #226d9a;
    --gold: #c8b274;
    --ink: #111111;
    --faint: #e6e7e6;
  }
  * { margin: 0; padding: 0; box-sizing: border-box; }
  html, body {
    width: 1200px; height: 1200px; overflow: hidden;
    background: var(--backdrop);
  }
  .canvas { position: relative; width: 1200px; height: 1200px; }

  .card { position: absolute; left: 246px; width: 709px; height: 405px; overflow: hidden; }
  .card--front { top: 148px; background: var(--card-front); }
  .card--back { top: 635px; background: var(--card-back); }

  .holder-name {
    position: absolute; left: 61px; top: 57px;
    font-family: "Tenor Sans", sans-serif; font-size: 22px; font-weight: 400;
    letter-spacing: 0.5px; color: var(--ink); line-height: 1; white-space: nowrap;
  }
  .holder-role {
    position: absolute; left: 61px; top: 85px;
    font-family: "Montserrat", sans-serif; font-size: 13px;
    color: var(--gold); line-height: 1;
  }

  .details { position: absolute; left: 63px; top: 172px; }
  .detail-row {
    position: absolute; left: 0; white-space: nowrap;
    font-family: "Fira Sans", sans-serif; line-height: 1;
  }
  .detail-label { position: absolute; left: 0; font-size: 12.5px; color: var(--gold); }
  .detail-value { position: absolute; left: 68px; font-size: 12.5px; color: var(--ink); }
  .detail-value--masked { font-size: 9px; top: -2px; letter-spacing: 0.5px; }

  .front-mark {
    position: absolute; left: 417px; top: 118px; width: 225px;
    font-family: "Tenor Sans", sans-serif; font-size: 30px; line-height: 1.15;
    color: var(--faint); text-align: center;
  }

  .office { position: absolute; left: 404px; top: 274px; font-family: "Fira Sans", sans-serif; font-style: normal; }
  .office-name { font-size: 12.5px; font-weight: 500; color: var(--gold); letter-spacing: 0.5px; }
  .office-line { font-size: 12.5px; color: var(--ink); margin-top: 8px; line-height: 1; white-space: nowrap; }

  .back-mark {
    position: absolute; left: 0; top: 160px; width: 709px; text-align: center;
    font-family: "Tenor Sans", sans-serif; font-size: 44px; line-height: 1;
    color: var(--gold); letter-spacing: 1px;
  }
  .logo-text {
    position: absolute; left: 0; top: 222px; width: 709px; text-align: center;
    font-family: "Tenor Sans", sans-serif; font-size: 14px; line-height: 1;
    color: var(--gold); letter-spacing: 2px;
  }
  .tagline {
    position: absolute; left: 0; top: 332px; width: 709px; text-align: center;
    font-family: "Tenor Sans", sans-serif; font-size: 15.5px; letter-spacing: 0.8px;
    color: var(--gold); line-height: 1; white-space: nowrap;
  }
</style>
</head>
<body>
<main class="canvas">
  <section class="card card--front">
    <h1 class="holder-name">DANA WHITFIELD</h1>
    <p class="holder-role">Proprietor</p>

    <div class="details">
      <div class="detail-row" style="top:0"><span class="detail-label">LBQC</span></div>
      <div class="detail-row" style="top:33px"><span class="detail-label">ACR</span><span class="detail-value detail-value--masked">************</span></div>
      <div class="detail-row" style="top:71px"><span class="detail-label">ABN</span><span class="detail-value detail-value--masked">************</span></div>
      <div class="detail-row" style="top:110px"><span class="detail-label">Mobile</span><span class="detail-value">+00 (482) 3307 000</span></div>
      <div class="detail-row" style="top:147px"><span class="detail-label">Email</span><span class="detail-value">harrowpeaklending@mail.com</span></div>
    </div>

    <p class="front-mark">Harrow Peak Lending</p>

    <address class="office">
      <p class="office-name">Harrow Peak Lending</p>
      <p class="office-line">88 Lantern Row 2nd Building, City, CA -&nbsp; 12345</p>
      <p class="office-line">United States</p>
    </address>
  </section>

  <section class="card card--back">
    <p class="back-mark">Harrow Peak Lending</p>
    <p class="logo-text">home, business, asset finance</p>
    <p class="tagline">DIP FINANCE &amp; MORTGAGE BROKING MANAGEMENT</p>
  </section>
</main>
</body>
</html>
```